concept design for a website homepage

Hi, we are looking for a design for Homepage for our childcare centre
We want something really progressive, edgy, modern and premium. We want this website to standout but not cluttered. We only need a Homepage concept design for the below measurements.
1366 Wx768 H
The call to action is join our community
We like the idea of a split screen
Divided into 4 sections screen with the below
Locations and Enrolments
Kestrel
Careers
Partnerships
We like angles and shapes, particularly triangles in the designs in the attached examples.
Our company font is Hands of Sean
Have attached some designs that we like the look and feel of and some of our designs from our flyers and some images to use, you don't need to choose all the images, just whatever works with your design.
We have a STEM focus at our centres so something sciency would be great.
Consider in the design will be viewed on desktop and mobile phones
1 page

```html
<!DOCTYPE html>
<html lang="en">
<head>
<meta charset="utf-8">
<title>Sunbeam Kindergarten</title>
<link href="https://fonts.googleapis.com/css2?family=Montserrat:wght@400;500;700&family=Roboto:wght@400;500&display=swap" rel="stylesheet">
<style>
:root{
  --blue:#00a3ea;
  --white:#ffffff;
  --ink:#2b2b2b;
  --muted:#6b6b6b;
  --line:#9a9a9a;
  --navy:#1d2a55;
}
*{box-sizing:border-box;margin:0;padding:0}
html,body{width:1200px;height:3329px;overflow:hidden;background:var(--white)}
body{position:relative;font-family:'Roboto',sans-serif;color:var(--ink)}
.abs{position:absolute}
.fill{position:absolute}
a{text-decoration:none}

/* hero */
.hero-panel{left:0;top:0;width:501px;height:674px;background:var(--blue)}
.hero-photo{left:501px;top:0;width:699px;height:674px;
  background:
    radial-gradient(ellipse 260px 170px at 58% 18%, rgba(236,196,40,.95), rgba(236,196,40,0) 70%),
    radial-gradient(ellipse 230px 150px at 47% 60%, rgba(230,120,70,.85), rgba(230,120,70,0) 70%),
    radial-gradient(ellipse 330px 300px at 82% 72%, rgba(20,95,170,.95), rgba(20,95,170,0) 72%),
    radial-gradient(ellipse 200px 260px at 96% 30%, rgba(90,70,50,.9), rgba(90,70,50,0) 70%),
    radial-gradient(ellipse 220px 160px at 10% 85%, rgba(60,45,25,.9), rgba(60,45,25,0) 70%),
    linear-gradient(135deg,#8a6a3a 0%,#d7b46a 40%,#c79a5a 60%,#3a5f90 100%)}
.social-box{left:951px;top:0;width:249px;height:88px;background:var(--blue);display:flex;align-items:center;justify-content:center;gap:24px}
.social-tag{width:44px;height:36px;border:2px solid var(--white);color:var(--white);font:500 12px 'Montserrat',sans-serif;display:flex;align-items:center;justify-content:center}
.menu-icon{left:16px;top:28px}
.brand{left:71px;top:34px;color:var(--white);font:700 15px 'Montserrat',sans-serif;display:flex;align-items:center;gap:6px}
.brand .dot{width:14px;height:14px;border-radius:50%;background:#ffd400}
.hero-title{left:72px;top:210px;color:var(--white);font:500 52px 'Montserrat',sans-serif;letter-spacing:1px}
.hero-sub{left:72px;top:274px;color:var(--white);font:500 28px 'Montserrat',sans-serif}
.hero-text{left:71px;top:334px;width:400px;color:var(--white);font-size:13.5px;line-height:21px}
.btn-white{left:71px;top:435px;width:178px;height:60px;background:var(--white);color:var(--blue);font:400 21px 'Montserrat',sans-serif;display:flex;align-items:center;justify-content:center}
.link-white{left:279px;top:451px;color:var(--white);font:400 21px 'Montserrat',sans-serif;text-decoration:underline}

/* locations */
.loc-band{left:608px;top:674px;width:592px;height:681px;background:var(--blue)}
.map{left:544px;top:775px;width:555px;height:472px;
  background:
    radial-gradient(ellipse 200px 90px at 55% 100%, rgba(168,222,150,.95), rgba(168,222,150,0) 75%),
    radial-gradient(ellipse 90px 60px at 70% 6%, rgba(190,225,170,.9), rgba(190,225,170,0) 75%),
    radial-gradient(ellipse 180px 170px at 72% 50%, rgba(214,214,210,1), rgba(214,214,210,0) 75%),
    radial-gradient(ellipse 140px 200px at 20% 45%, rgba(226,226,222,1), rgba(226,226,222,0) 75%),
    linear-gradient(160deg,#ececea,#e0e0dc 60%,#d6e8cc 100%)}
.sec-title{color:var(--blue);font:700 36px/53px 'Montserrat',sans-serif}
.loc-title{left:72px;top:775px}
.field{left:71px;width:386px;border-bottom:1.5px solid var(--line);color:var(--muted);font-size:16px;padding:0 1px 14px}
.btn-blue{background:var(--blue);color:var(--white);font:400 21px 'Montserrat',sans-serif;display:flex;align-items:center;justify-content:center}
.signup{left:71px;top:1247px;width:211px;height:61px}
.contact-row{top:1285px;color:var(--white);font:500 21px 'Roboto',sans-serif;display:flex;align-items:center;gap:14px}
.icon-box{width:34px;height:34px;background:var(--white);display:flex;align-items:center;justify-content:center}

/* kestrel */
.kestrel{left:0;top:1355px;width:1200px;height:674px;
  background:
    radial-gradient(ellipse 260px 200px at 30% 80%, rgba(150,110,60,.55), rgba(150,110,60,0) 75%),
    radial-gradient(ellipse 200px 200px at 4% 30%, rgba(110,130,80,.5), rgba(110,130,80,0) 75%),
    radial-gradient(ellipse 180px 260px at 97% 45%, rgba(80,110,160,.55), rgba(80,110,160,0) 75%),
    radial-gradient(ellipse 300px 220px at 60% 90%, rgba(70,60,140,.6), rgba(70,60,140,0) 75%),
    linear-gradient(100deg,#3a3446 0%,#2c2a4a 40%,#1f2a5c 70%,#2a2e58 100%)}
.kestrel-shade{left:0;top:1355px;width:560px;height:674px;background:linear-gradient(90deg,rgba(20,18,35,.35),rgba(20,18,35,0))}
.kestrel-shot-a{left:555px;top:1400px;width:431px;height:279px;
  background:
    radial-gradient(circle 70px at 48% 72%, rgba(200,210,255,.9), rgba(200,210,255,0) 80%),
    radial-gradient(ellipse 120px 60px at 50% 20%, rgba(255,120,170,.7), rgba(255,120,170,0) 80%),
    radial-gradient(ellipse 90px 140px at 12% 50%, rgba(40,60,220,.9), rgba(40,60,220,0) 80%),
    linear-gradient(180deg,#2a2fa8,#5b58d8 50%,#14143a)}
.kestrel-shot-b{left:633px;top:1679px;width:430px;height:317px;
  background:
    radial-gradient(ellipse 200px 70px at 50% 92%, rgba(230,150,90,.95), rgba(230,150,90,0) 80%),
    radial-gradient(ellipse 90px 130px at 25% 45%, rgba(235,235,250,.8), rgba(235,235,250,0) 80%),
    radial-gradient(ellipse 90px 130px at 58% 48%, rgba(230,225,245,.75), rgba(230,225,245,0) 80%),
    radial-gradient(ellipse 70px 160px at 95% 40%, rgba(60,80,200,.8), rgba(60,80,200,0) 80%),
    linear-gradient(180deg,#3a3a90,#7a86c8 55%,#c89a6a)}
.kestrel-brand{left:71px;top:1520px;color:var(--white);font:700 44px 'Montserrat',sans-serif;letter-spacing:3px;display:flex;align-items:center;gap:12px}
.kestrel-brand .dot{width:26px;height:26px;border-radius:50%;background:#ffd400}
.kestrel-tag{left:86px;top:1584px;color:var(--white);font:500 18px 'Montserrat',sans-serif}
.kestrel-title{left:71px;top:1634px;width:470px;color:var(--white);font:700 36px/46px 'Montserrat',sans-serif}
.kestrel-text{left:71px;top:1750px;width:440px;color:var(--white);font-size:14px;line-height:21px}

/* career */
.career-band{left:0;top:2029px;width:429px;height:593px;background:var(--blue)}
.career-photo{left:71px;top:2086px;width:610px;height:482px;
  background:
    radial-gradient(ellipse 150px 200px at 18% 40%, rgba(250,248,245,.95), rgba(250,248,245,0) 75%),
    radial-gradient(ellipse 130px 120px at 58% 45%, rgba(248,246,242,.9), rgba(248,246,242,0) 75%),
    radial-gradient(ellipse 260px 110px at 45% 88%, rgba(205,160,110,.95), rgba(205,160,110,0) 75%),
    radial-gradient(ellipse 120px 80px at 40% 78%, rgba(230,90,110,.55), rgba(230,90,110,0) 75%),
    radial-gradient(ellipse 100px 200px at 90% 30%, rgba(200,170,120,.8), rgba(200,170,120,0) 75%),
    linear-gradient(135deg,#ece6dc,#dcc8ae 45%,#c9a27c 100%)}
.career-title{left:730px;top:2112px}
.career-text{left:730px;top:2180px;width:390px;font-size:13.5px;line-height:21px}
.ticks{left:730px;top:2310px;width:400px;list-style:none;font-size:13.5px;line-height:21px}
.ticks li{display:flex;gap:14px;margin-bottom:18px}
.ticks svg{flex:none;margin-top:0}
.join{left:730px;top:2459px;width:212px;height:61px}

/* partnerships */
.partners{left:0;top:2622px;width:1200px;height:410px;
  background:
    radial-gradient(ellipse 300px 160px at 52% 75%, rgba(130,140,180,.55), rgba(130,140,180,0) 75%),
    radial-gradient(ellipse 260px 240px at 8% 40%, rgba(70,80,120,.7), rgba(70,80,120,0) 75%),
    radial-gradient(ellipse 260px 240px at 90% 30%, rgba(55,65,105,.7), rgba(55,65,105,0) 75%),
    linear-gradient(120deg,#3c4670,#2a3563 50%,#1e2a55)}
.partners-title{left:0;top:2690px;width:1200px;text-align:center;color:var(--white);font:700 36px 'Montserrat',sans-serif}
.partners-text{left:205px;top:2778px;width:790px;text-align:center;color:var(--white);font-size:13.5px;line-height:21px}
.btn-outline{left:495px;top:2900px;width:210px;height:60px;border:3px solid var(--white);color:var(--white);font:400 21px 'Montserrat',sans-serif;display:flex;align-items:center;justify-content:center}

/* footer */
.footer{left:0;top:3032px;width:1200px;height:297px;background:var(--blue)}
.footer-brand{left:142px;top:3128px;color:var(--white);font:700 20px 'Montserrat',sans-serif;display:flex;align-items:center;gap:8px}
.footer-brand .dot{width:18px;height:18px;border-radius:50%;background:#ffd400}
.foot-head{color:var(--white);font:500 20px 'Montserrat',sans-serif}
.foot-link{color:var(--white);font-size:15px}
.foot-contact{left:784px;color:var(--white);font-size:13.5px;display:flex;align-items:center;gap:12px}
.foot-social{left:784px;top:3190px;display:flex;gap:22px}
.foot-social .social-tag{width:48px;height:36px}
.foot-rule{left:71px;top:3254px;width:1059px;height:1px;background:rgba(255,255,255,.7)}
.copyright{left:0;top:3282px;width:1200px;text-align:center;color:var(--white);font-size:13.5px}
</style>
</head>
<body>

<!-- hero -->
<div class="fill hero-panel"></div>
<div class="fill hero-photo" role="img" aria-label="Photo of a child in a hard hat and safety goggles using a drill"></div>
<div class="abs social-box">
  <span class="social-tag">Feed</span><span class="social-tag">Chirp</span><span class="social-tag">Lens</span>
</div>
<svg class="abs menu-icon" width="34" height="32" viewBox="0 0 34 32" aria-label="Menu">
  <rect x="1" y="1" width="32" height="30" fill="none" stroke="#fff" stroke-width="2"/>
  <path d="M7 10h20M7 16h20M7 22h20" stroke="#fff" stroke-width="2.5"/>
</svg>
<div class="abs brand"><span class="dot"></span>Sunbeam</div>
<h1 class="abs hero-title">SUNBEAM</h1>
<div class="abs hero-sub">KINDERGARTEN</div>
<p class="abs hero-text">We work closely with each family to meet the individual needs of their child to maintain their daily routine in a caring and nurturing environment where children feel safe and secure.</p>
<a class="abs btn-white">Contact Us</a>
<a class="abs link-white">Learn More</a>

<!-- locations -->
<div class="fill loc-band"></div>
<div class="fill map" role="img" aria-label="Street map showing the centre location"></div>
<h2 class="abs sec-title loc-title">LOCATIONS &amp;<br>ENROLMENTS</h2>
<div class="abs field" style="top:924px">Name</div>
<div class="abs field" style="top:996px">Address</div>
<div class="abs field" style="top:1068px">Phone Numbers</div>
<div class="abs field" style="top:1140px">Email</div>
<a class="abs btn-blue signup">Sign Up</a>
<div class="abs contact-row" style="left:645px">
  <span class="icon-box"><svg width="20" height="20" viewBox="0 0 24 24"><path d="M6.6 10.8a15 15 0 0 0 6.6 6.6l2.2-2.2c.3-.3.7-.4 1-.2 1.1.4 2.3.6 3.6.6.6 0 1 .4 1 1V20c0 .6-.4 1-1 1A17 17 0 0 1 3 4c0-.6.4-1 1-1h3.5c.6 0 1 .4 1 1 0 1.3.2 2.5.6 3.6.1.3 0 .7-.2 1z" fill="#00a3ea"/></svg></span>9400 1234
</div>
<div class="abs contact-row" style="left:839px">
  <span class="icon-box"><svg width="20" height="20" viewBox="0 0 24 24"><path d="M12 3 2 12h3v8h5v-5h4v5h5v-8h3z" fill="#00a3ea"/></svg></span>14-16 Wattle Crescent, Linden
</div>

<!-- kestrel -->
<div class="fill kestrel" role="img" aria-label="Photo of the science discovery centre interior"></div>
<div class="fill kestrel-shade"></div>
<div class="fill kestrel-shot-a" role="img" aria-label="Photo of a glowing science exhibit"></div>
<div class="fill kestrel-shot-b" role="img" aria-label="Photo of children in lab coats at a sand table"></div>
<div class="abs kestrel-brand"><span class="dot"></span>KESTREL</div>
<div class="abs kestrel-tag">Centre of Imagination</div>
<h2 class="abs kestrel-title">Exclusive to the Sunbeam Community</h2>
<p class="abs kestrel-text">Lorem ipsum dolor sit amet, consectetur adipiscing elit. Etiam eu turpis molestie, dictum est a, mattis tellus. Sed dignissim, metus nec fringilla accumsan, risus sem sollicitudin lacus, ut interdum tellus elit sed risus.</p>

<!-- career -->
<div class="fill career-band"></div>
<div class="fill career-photo" role="img" aria-label="Photo of a teacher with children drawing at a table"></div>
<h2 class="abs sec-title career-title">CAREER</h2>
<p class="abs career-text">Lorem ipsum dolor sit amet, consectetur adipiscing elit. Etiam eu turpis molestie, dictum est a, mattis tellus. Sed dignissim, metus nec fringilla accumsan, risus sem sollicitudin lacus, ut interdum tellus elit sed risus. Maecenas eget condimentum velit, sit amet feugiat lectus.</p>
<ul class="abs ticks">
  <li><svg width="20" height="20" viewBox="0 0 20 20"><circle cx="10" cy="10" r="10" fill="#00a3ea"/><path d="M5.5 10.2l3 3 6-6" stroke="#fff" stroke-width="2" fill="none"/></svg>Lorem ipsum dolor sit amet, consectetur.</li>
  <li><svg width="20" height="20" viewBox="0 0 20 20"><circle cx="10" cy="10" r="10" fill="#00a3ea"/><path d="M5.5 10.2l3 3 6-6" stroke="#fff" stroke-width="2" fill="none"/></svg>Lorem ipsum dolor sit amet, consectetur adipiscing.</li>
  <li><svg width="20" height="20" viewBox="0 0 20 20"><circle cx="10" cy="10" r="10" fill="#00a3ea"/><path d="M5.5 10.2l3 3 6-6" stroke="#fff" stroke-width="2" fill="none"/></svg>Lorem ipsum dolor sit amet, consectetur adipiscing elit. Etiam eu turpis molestie.</li>
</ul>
<a class="abs btn-blue join">Join With Us</a>

<!-- partnerships -->
<div class="fill partners" role="img" aria-label="Photo of two people shaking hands"></div>
<h2 class="abs partners-title">PARTNERSHIPS</h2>
<p class="abs partners-text">Lorem ipsum dolor sit amet, consectetur adipiscing elit. Etiam eu turpis molestie, dictum est a, mattis tellus. Sed dignissim, metus nec fringilla accumsan, risus sem sollicitudin lacus, ut interdum tellus elit sed risus. Maecenas eget condimentum velit, sit amet feugiat lectus. Class aptent taciti sociosqu ad litora torquent per conubia nostra.</p>
<a class="abs btn-outline">Learn More</a>

<!-- footer -->
<div class="fill footer"></div>
<div class="abs footer-brand"><span class="dot"></span>Sunbeam</div>
<div class="abs foot-head" style="left:389px;top:3062px">Quick Links</div>
<a class="abs foot-link" style="left:393px;top:3105px">Home</a>
<a class="abs foot-link" style="left:393px;top:3141px">Locations &amp; Enrolments</a>
<a class="abs foot-link" style="left:393px;top:3177px">Kestrel</a>
<a class="abs foot-link" style="left:606px;top:3105px">Career</a>
<a class="abs foot-link" style="left:606px;top:3141px">Partnerships</a>
<div class="abs foot-head" style="left:784px;top:3062px">Contact Us</div>
<div class="abs foot-contact" style="top:3105px">
  <svg width="18" height="16" viewBox="0 0 24 20"><path d="M2 3l6-2 8 2 6-2v16l-6 2-8-2-6 2z M8 1v16 M16 3v16" fill="none" stroke="#fff" stroke-width="1.6"/></svg>14-16 Wattle Crescent, Linden
</div>
<div class="abs foot-contact" style="top:3141px">
  <svg width="16" height="16" viewBox="0 0 24 24"><path d="M6.6 10.8a15 15 0 0 0 6.6 6.6l2.2-2.2c.3-.3.7-.4 1-.2 1.1.4 2.3.6 3.6.6.6 0 1 .4 1 1V20c0 .6-.4 1-1 1A17 17 0 0 1 3 4c0-.6.4-1 1-1h3.5c.6 0 1 .4 1 1 0 1.3.2 2.5.6 3.6.1.3 0 .7-.2 1z" fill="#fff"/></svg>9400 1234
</div>
<div class="abs foot-social">
  <span class="social-tag">Feed</span><span class="social-tag">Chirp</span><span class="social-tag">Lens</span>
</div>
<div class="fill foot-rule"></div>
<p class="abs copyright">Copyrights © 2022, Sunbeam Kindergarten. All rights reserved. Terms &amp; Conditions</p>

</body>
</html>
```